Cake Bakery needs Large New Vibrant Window Decals

Our cake bakery is moving to a new location. We want to place window decals (vinyl) on 7 separate windows that are all the same size. (Image is attached for your reference. The windows are the ones within the red outline.)

The windows are approximately 76 inches tall and 98 inches wide. We have uploaded an image of the storefront to show you the 7 windows that need be to covered.

There are also 2 side by side doors that need a decals too. We have uploaded a logo we are using. You are allowed to change the logo color to better coordinate with a design you can create.

We want the colors to be bright and cheerful. You can see our current bakery website at brindlewoodsweets.example. ( I included the sign above our bakery if that helps you.)

Do not use any images of cakes or other bakery products in your design.

The graphics can be simple and clean or can be vivid and loud. We will consider all concepts.

You can create one design to be duplicated for each window or create a design that would flow across all the windows in a landscape effect.

Target Market(s)

People who purchase cakes for any occasion.

Industry/Entity Type

Bakery

Requirements
Must have
• Must have the logo on each window
Nice to have
• Open to any concepts
Should not have
• No images of cakes or other bakery products. The graphics must stand the test of time for the next 10 years.

```html
<!DOCTYPE html>
<html lang="en">
<head>
<meta charset="utf-8">
<title>Brindlewood Sweets – Window Decal Set</title>
<link rel="stylesheet" href="https://fonts.googleapis.com/css2?family=Fredoka:wght@600&display=swap">
<style>
  :root {
    --backdrop: #d9d9d9;
    --decal-white: #ffffff;
    --coral: #f07e7b;
    --plum: #542a7a;
  }
  html, body {
    margin: 0;
    padding: 0;
    width: 1200px;
    height: 240px;
    overflow: hidden;
    background: var(--backdrop);
  }
  .decal-strip {
    position: relative;
    width: 1200px;
    height: 240px;
  }
  .window-decal, .door-decal {
    position: absolute;
    top: 56px;
    background: var(--decal-white);
    overflow: hidden;
  }
  .window-decal { width: 139px; height: 108px; }
  .door-decal { width: 132px; height: 162px; }
  .decal-art {
    position: absolute;
    inset: 0;
    width: 100%;
    height: 100%;
  }
  .wordmark {
    position: absolute;
    transform: translate(-50%, -50%);
    margin: 0;
    font-family: "Fredoka", sans-serif;
    font-weight: 600;
    color: var(--coral);
    text-align: center;
    line-height: 1;
    white-space: nowrap;
  }
  .window-decal .wordmark { left: 50%; top: 71%; font-size: 10px; }
  .door-decal .wordmark { top: 54%; font-size: 7px; }
  .door-decal .wordmark.left { left: 30%; }
  .door-decal .wordmark.right { left: 71%; }
  .coral-fill { fill: var(--coral); }
  .plum-fill { fill: var(--plum); }
</style>
</head>
<body>
<svg width="0" height="0" style="position:absolute" aria-hidden="true">
  <defs>
    <symbol id="sparkle" viewBox="-10 -10 20 20">
      <path class="plum-fill" d="M0 -10C1.5 -2 2 -1.5 10 0C2 1.5 1.5 2 0 10C-1.5 2 -2 1.5 -10 0C-2 -1.5 -1.5 -2 0 -10Z"/>
    </symbol>
    <symbol id="wave-swoop" viewBox="0 0 298 231">
      <path class="coral-fill" d="M0 0H298V110C275 118 255 122 240 122C270 100 295 80 290 60C285 50 250 55 200 65C150 75 100 82 70 75C40 68 22 50 0 10Z"/>
      <path class="plum-fill" d="M20 62C40 90 80 100 110 95C160 88 210 72 250 70C200 80 150 95 110 100C70 104 40 95 20 62Z"/>
    </symbol>
    <symbol id="wave-peak" viewBox="0 0 298 231">
      <path class="coral-fill" d="M0 0H298V70C240 72 180 75 140 80C100 84 70 75 65 60C62 50 64 40 62 38C50 55 30 75 0 95Z"/>
      <path class="plum-fill" d="M80 88C130 96 200 82 298 76V82C200 88 140 100 80 88Z"/>
      <path class="plum-fill" d="M0 100C20 90 40 80 60 65C40 85 20 95 0 108Z"/>
    </symbol>
    <symbol id="wave-curl" viewBox="0 0 298 231">
      <path class="coral-fill" d="M0 0H298V88C240 74 170 60 110 55C80 52 50 55 45 65C40 75 60 82 70 80C45 90 30 85 0 75Z"/>
      <path class="plum-fill" d="M80 57C150 58 230 72 298 88V95C230 80 150 62 80 57Z"/>
      <path class="plum-fill" d="M0 75C25 82 45 95 65 120C45 100 25 88 0 82Z"/>
    </symbol>
    <symbol id="door-waves" viewBox="0 0 284 347">
      <path class="coral-fill" d="M0 0H284V80C240 82 200 85 185 78C175 73 180 62 180 55C180 45 170 30 155 22C160 40 150 60 130 70C100 82 50 80 0 78Z"/>
      <path class="plum-fill" d="M0 82C50 92 110 92 140 78C120 95 60 98 0 90Z"/>
      <path class="plum-fill" d="M140 112C190 118 240 108 284 100V106C240 116 190 122 140 112Z"/>
      <path class="coral-fill" d="M0 347H284V300C270 270 240 265 215 268C190 272 160 285 155 300C150 290 140 265 120 255C100 245 60 240 30 235C70 250 100 268 95 295C90 315 70 320 50 318C30 316 10 310 0 320Z"/>
      <path class="plum-fill" d="M160 275C180 262 210 258 245 262C215 262 190 270 170 285Z"/>
    </symbol>
  </defs>
</svg>

<main class="decal-strip">
  <section class="window-decal" style="left:19px">
    <svg class="decal-art" viewBox="0 0 298 231" preserveAspectRatio="none">
      <use href="#wave-swoop" width="298" height="231"/>
      <use href="#sparkle" x="204" y="96" width="34" height="34"/>
      <use href="#sparkle" x="36" y="168" width="30" height="30"/>
    </svg>
    <p class="wordmark">Brindlewood<br>Sweets</p>
  </section>

  <section class="window-decal" style="left:166px">
    <svg class="decal-art" viewBox="0 0 298 231" preserveAspectRatio="none">
      <use href="#wave-peak" width="298" height="231"/>
      <use href="#sparkle" x="203" y="94" width="34" height="34"/>
      <use href="#sparkle" x="36" y="170" width="30" height="30"/>
    </svg>
    <p class="wordmark">Brindlewood<br>Sweets</p>
  </section>

  <section class="window-decal" style="left:313px">
    <svg class="decal-art" viewBox="0 0 298 231" preserveAspectRatio="none">
      <use href="#wave-curl" width="298" height="231"/>
      <use href="#sparkle" x="202" y="92" width="34" height="34"/>
      <use href="#sparkle" x="36" y="170" width="30" height="30"/>
    </svg>
    <p class="wordmark">Brindlewood<br>Sweets</p>
  </section>

  <section class="door-decal" style="left:460px">
    <svg class="decal-art" viewBox="0 0 284 347" preserveAspectRatio="none">
      <use href="#door-waves" width="284" height="347"/>
      <use href="#sparkle" x="138" y="222" width="24" height="24"/>
    </svg>
    <p class="wordmark left">Brindlewood<br>Sweets</p>
    <p class="wordmark right">Brindlewood<br>Sweets</p>
  </section>

  <section class="window-decal" style="left:601px">
    <svg class="decal-art" viewBox="0 0 298 231" preserveAspectRatio="none">
      <g transform="translate(298 0) scale(-1 1)"><use href="#wave-peak" width="298" height="231"/></g>
      <use href="#sparkle" x="66" y="86" width="34" height="34"/>
      <use href="#sparkle" x="230" y="166" width="30" height="30"/>
    </svg>
    <p class="wordmark">Brindlewood<br>Sweets</p>
  </section>

  <section class="window-decal" style="left:748px">
    <svg class="decal-art" viewBox="0 0 298 231" preserveAspectRatio="none">
      <use href="#wave-peak" width="298" height="231"/>
      <use href="#sparkle" x="200" y="92" width="34" height="34"/>
      <use href="#sparkle" x="36" y="172" width="30" height="30"/>
    </svg>
    <p class="wordmark">Brindlewood<br>Sweets</p>
  </section>

  <section class="window-decal" style="left:895px">
    <svg class="decal-art" viewBox="0 0 298 231" preserveAspectRatio="none">
      <g transform="translate(298 0) scale(-1 1)"><use href="#wave-curl" width="298" height="231"/></g>
      <use href="#sparkle" x="194" y="78" width="34" height="34"/>
      <use href="#sparkle" x="30" y="158" width="30" height="30"/>
    </svg>
    <p class="wordmark">Brindlewood<br>Sweets</p>
  </section>

  <section class="window-decal" style="left:1042px">
    <svg class="decal-art" viewBox="0 0 298 231" preserveAspectRatio="none">
      <g transform="translate(298 0) scale(-1 1)"><use href="#wave-swoop" width="298" height="231"/></g>
      <use href="#sparkle" x="62" y="90" width="34" height="34"/>
      <use href="#sparkle" x="232" y="168" width="30" height="30"/>
    </svg>
    <p class="wordmark">Brindlewood<br>Sweets</p>
  </section>
</main>
</body>
</html>
```